Oven Cleaning flyer design

Hi there,
I need help designing a letterbox flyer. It needs to be DL size.
I have attached a rough design made with Chat GPT.
Would like back and front, have my business colors.
Please find attached mock up of what I would roughly like.
Also find attached logo.
Thank you

Target Market(s)

Home owners over 40

Industry/Entity Type

Cleaning

Requirements
Must have
• Logo, before after of oven, brand colors

```html
<!DOCTYPE html>
<html lang="en">
<head>
<meta charset="utf-8">
<title>Hearth Shine Co – DL Flyer Front and Back</title>
<link rel="stylesheet" href="https://fonts.googleapis.com/css2?family=Montserrat:wght@400;500;600;700;800&display=swap">
<style>
:root{
  --navy:#1f2a55;
  --teal:#48c2c7;
  --ink:#111111;
  --white:#ffffff;
  --backdrop:#6f6f6f;
  --gold:#d9a92a;
  --star:#1fa3e0;
}
*{box-sizing:border-box;margin:0;padding:0}
html,body{width:1200px;height:2291px;overflow:hidden}
body{
  background:var(--backdrop);
  font-family:'Montserrat',sans-serif;
  color:var(--ink);
  position:relative;
}
.flyer{
  position:absolute;top:590px;width:540px;height:1110px;
  background:var(--white);
  display:flex;flex-direction:column;
  box-shadow:0 10px 30px rgba(0,0,0,.35);
}
.flyer--front{left:40px}
.flyer--back{left:620px}

.brand{height:175px;flex:none;display:flex;align-items:center;justify-content:center;gap:18px}
.brand__dot{width:64px;height:64px;border-radius:50%;background:var(--teal)}
.brand__name{font-weight:800;font-size:40px;color:var(--teal);letter-spacing:1px;line-height:1}

.intro{height:272px;flex:none;background:var(--navy);color:var(--white)}
.intro--front{text-align:center;padding:24px 26px 0}
.headline{font-weight:500;font-size:56px;line-height:1;letter-spacing:-.5px}
.headline strong{display:block;font-weight:800;color:var(--teal);margin-top:2px}
.intro__text{font-size:18px;line-height:1.35;margin:16px auto 0;max-width:460px;font-weight:500}

.compare-labels{height:45px;flex:none;background:var(--teal);display:flex;color:var(--white);font-weight:800;font-size:27px;letter-spacing:.5px}
.compare-labels span{flex:1;text-align:center;line-height:45px}

.compare{height:359px;flex:none;display:flex;position:relative}
.compare__photo{flex:1}
.compare__photo--before{background:linear-gradient(160deg,#5b5b58 0%,#7a5a35 45%,#8c6a3f 60%,#b9b5ae 100%)}
.compare__photo--after{background:linear-gradient(160deg,#4a4d52 0%,#9ea2a7 40%,#d9dadc 70%,#efefef 100%)}
.badge{position:absolute;left:50%;bottom:-10px;transform:translateX(-50%);width:90px;height:90px;border-radius:50%;background:var(--gold)}

.cta{height:179px;flex:none;display:flex;flex-direction:column;align-items:center;justify-content:center;text-align:center}
.cta__lead{font-weight:700;font-size:29px;line-height:1.02}
.cta__phone{display:flex;align-items:center;gap:12px;margin-top:8px;font-weight:700;font-size:51px;color:var(--teal);line-height:1}
.cta__phone svg{width:48px;height:48px}

.footer{height:80px;flex:none;margin-top:auto;background:var(--teal);display:flex;align-items:center;justify-content:center;gap:8px;font-weight:700;font-size:25px;color:var(--ink)}
.footer svg{width:26px;height:26px}

.intro--back{padding:22px 36px 0}
.why{font-size:32px;line-height:1;font-weight:700}
.why span{display:block;font-weight:500;color:var(--teal)}
.why-text{font-size:17.5px;line-height:1.45;text-align:justify;margin-top:18px;font-weight:500}

.offer{padding:14px 48px 0;flex:1}
.offer__price{font-weight:800;font-size:124px;color:var(--teal);line-height:1;letter-spacing:-3px}
.offer__sub{font-weight:600;font-size:36px;line-height:1;margin-top:-2px}
.perks{list-style:none;margin-top:18px}
.perks li{display:flex;align-items:center;gap:12px;font-weight:700;font-size:20px;line-height:34px}
.perks svg{width:26px;height:26px}
.extras{margin-top:26px;font-size:35px;line-height:1.03;font-weight:500;color:var(--teal)}
.extras b{color:var(--ink);font-weight:800}
.divider{height:3px;margin:34px -16px 0;background:linear-gradient(90deg,transparent,#4a5170 15%,#4a5170 85%,transparent)}
.flyer--back .cta{height:auto;padding:18px 0 34px}
</style>
</head>
<body>

<section class="flyer flyer--front">
  <header class="brand">
    <span class="brand__dot"></span>
    <span class="brand__name">HEARTH SHINE CO</span>
  </header>
  <div class="intro intro--front">
    <h1 class="headline">Bring Your Oven<strong>Back to Life</strong></h1>
    <p class="intro__text">Professional, non-caustic oven cleaning that removes built-up grease, smoke, and burnt grime-leaving your oven looking fresh again.</p>
  </div>
  <div class="compare-labels"><span>BEFORE</span><span>AFTER</span></div>
  <div class="compare">
    <div class="compare__photo compare__photo--before" role="img" aria-label="Photo of a dirty oven interior with burnt grease on the door glass"></div>
    <div class="compare__photo compare__photo--after" role="img" aria-label="Photo of the same oven interior cleaned and shining"></div>
    <span class="badge" role="img" aria-label="Satisfaction guarantee badge"></span>
  </div>
  <div class="cta">
    <p class="cta__lead">Call Now for<br>Fast, Professional Service</p>
    <p class="cta__phone">
      <svg viewBox="0 0 48 48" aria-hidden="true"><circle cx="24" cy="24" r="23" fill="var(--ink)"/><path d="M17 12c2 0 3 4 4 6s-2 3-2 4c1 3 4 6 7 7 1 0 2-3 4-2s6 2 6 4-3 5-6 5c-9 0-19-10-19-19 0-3 3-5 6-5z" fill="var(--white)"/></svg>
      0400 582 194
    </p>
  </div>
  <footer class="footer">
    <svg viewBox="0 0 26 26" aria-hidden="true" fill="none" stroke="var(--ink)" stroke-width="2"><circle cx="13" cy="13" r="11"/><ellipse cx="13" cy="13" rx="5" ry="11"/><path d="M2 13h22M4 7h18M4 19h18"/></svg>
    www.hearthshineco.com.au
  </footer>
</section>

<section class="flyer flyer--back">
  <header class="brand">
    <span class="brand__dot"></span>
    <span class="brand__name">HEARTH SHINE CO</span>
  </header>
  <div class="intro intro--back">
    <h2 class="why">why choose<span>Hearth Shine Co?</span></h2>
    <p class="why-text">we're a local family business providing professional, non-caustic oven cleaning across Sunshine Coast. Using specialized-equipment and proven cleaning methods, we remove heavy grease, carbon build-up, smoke residue, restoring your oven safely and effectively.</p>
  </div>
  <div class="offer">
    <p class="offer__price">$10 off</p>
    <p class="offer__sub">your first clean</p>
    <ul class="perks">
      <li><svg viewBox="0 0 26 26" aria-hidden="true"><path d="M13 0l3 10 10 3-10 3-3 10-3-10L0 13l10-3z" fill="var(--star)"/></svg>Reliable Service</li>
      <li><svg viewBox="0 0 26 26" aria-hidden="true"><path d="M13 0l3 10 10 3-10 3-3 10-3-10L0 13l10-3z" fill="var(--star)"/></svg>Non-Caustic Cleaning</li>
      <li><svg viewBox="0 0 26 26" aria-hidden="true"><path d="M13 0l3 10 10 3-10 3-3 10-3-10L0 13l10-3z" fill="var(--star)"/></svg>Satisfaction Guaranteed</li>
    </ul>
    <p class="extras">We also clean <b>cooktops,</b><br><b>rangehoods</b> and <b>BBQs</b></p>
    <div class="divider"></div>
    <div class="cta">
      <p class="cta__lead">Call Now for<br>Fast, Professional Service</p>
      <p class="cta__phone">
        <svg viewBox="0 0 48 48" aria-hidden="true"><circle cx="24" cy="24" r="23" fill="var(--ink)"/><path d="M17 12c2 0 3 4 4 6s-2 3-2 4c1 3 4 6 7 7 1 0 2-3 4-2s6 2 6 4-3 5-6 5c-9 0-19-10-19-19 0-3 3-5 6-5z" fill="var(--white)"/></svg>
        0400 582 194
      </p>
    </div>
  </div>
  <footer class="footer">
    <svg viewBox="0 0 26 26" aria-hidden="true" fill="none" stroke="var(--ink)" stroke-width="2"><circle cx="13" cy="13" r="11"/><ellipse cx="13" cy="13" rx="5" ry="11"/><path d="M2 13h22M4 7h18M4 19h18"/></svg>
    www.hearthshineco.com.au
  </footer>
</section>

</body>
</html>
```